◆遺体の目的/概要
電子書籍(lumora)の表紙のデザインをお願いします。

◆画像のサイズ
表紙ファイルの理想的な寸法は2,560✕1,600ピクセルです。
注:画像の寸法は1,000✕625ピクセル以上であることが必要です。
画像の最大の寸法は10,000✕10,000ピクセルです。

◆タイトル
外国人と一緒に働くすべての人へ
「ミナト・ハーモニー・トーキング」
Bright Harbor Dialogue
少子高齢化の社会を生き残る強い会社を作る方法

◆著者
外国人ブリッジコーディネーター
村上 健二

◆本の内容
少子高齢化が進む社会にあって、
外国人労働者の必要性や、彼らが働きやす職場環境作りの必要性
どんなコミュニケーションが必要かという事を解説した本です。
※本文を参考資料として添付します。

◆デザイン要望
会社や企業向けなので、プロフェッショナルなイメージ
グローバルなイメージ(目を引く外国人の写真など)
でよろしくお願い致します。

※次点、次々点の方への参加報酬も設定いたします。

※その他、必要な情報がありましたらお問い合せください。

本文の内容に該当する登場人物のイメージを用いている点や
「強い会社を作る」という主なテーマが強調されていいる点など、
ぱっと見て分かりやすいものを選ばせていただきました。

ほんとにどれもセンスを感じられるものだったので、
選定するのに、とても時間がかかりました。
同じテーマで、こんなにも色々なアイデアがあること
その多様性に感動しました。
皆さんが時間をかけて、考えてくださったことに感謝致します。
今後も出版を考えていますので、また依頼の際は多くの方の提案をよろしくお願い致します!

```html
<!DOCTYPE html>
<html lang="ja">
<head>
<meta charset="utf-8">
<title>ミナト・ハーモニー・トーキング — 表紙</title>
<link rel="stylesheet" href="https://fonts.googleapis.com/css2?family=Shippori+Mincho+B1:wght@600;800&family=M+PLUS+Rounded+1c:wght@700;800&family=Noto+Sans+JP:wght@500;900&family=Caveat:wght@400&display=swap">
<style>
  :root {
    --teal: #2fb3b4;
    --teal-soft: #a3d7d8;
    --navy: #262a4b;
    --ink: #1f2340;
    --paper: #ffffff;
  }
  html, body { margin: 0; padding: 0; overflow: hidden; background: var(--paper); }
  .cover {
    position: relative;
    width: 750px;
    height: 1200px;
    overflow: hidden;
    background: var(--paper);
  }
  .tagline {
    position: absolute;
    top: 18px; left: 0; width: 100%;
    text-align: center;
    font-family: "M PLUS Rounded 1c", sans-serif;
    font-weight: 800;
    font-size: 31px;
    letter-spacing: 1px;
    color: var(--teal);
    margin: 0;
  }
  .title {
    position: absolute;
    top: 100px; left: 28px;
    margin: 0;
    font-family: "Shippori Mincho B1", serif;
    font-weight: 800;
    font-size: 74px;
    line-height: 88px;
    color: var(--ink);
    letter-spacing: -1px;
  }
  .title span { display: block; }
  .title-en {
    position: absolute;
    top: 175px; left: 330px;
    font-family: "Caveat", cursive;
    font-size: 62px;
    line-height: 56px;
    color: var(--teal-soft);
    transform: rotate(-11deg);
    transform-origin: left top;
    white-space: nowrap;
  }
  .title-en span { display: block; }
  .title-en span + span { padding-left: 40px; }
  .author {
    position: absolute;
    top: 378px; right: 30px;
    text-align: right;
  }
  .author-role {
    font-family: "Noto Sans JP", sans-serif;
    font-weight: 900;
    font-size: 17px;
    color: var(--teal);
    margin: 0;
  }
  .author-name {
    font-family: "Noto Sans JP", sans-serif;
    font-weight: 500;
    font-size: 28px;
    color: #111;
    margin: 2px 0 0;
    letter-spacing: 2px;
  }
  .photo {
    position: absolute;
    top: 439px; left: 0;
    width: 750px; height: 416px;
    background:
      radial-gradient(ellipse at 48% 30%, rgba(255,255,255,0.9) 0%, rgba(255,255,255,0) 30%),
      linear-gradient(90deg, #4f6f7e 0%, #9fb7bd 30%, #d6e3df 50%, #7fb3a8 75%, #3f7a74 100%);
  }
  .photo::after {
    content: "";
    position: absolute; inset: 0;
    background: linear-gradient(180deg, rgba(0,0,0,0) 55%, rgba(40,50,70,0.35) 100%);
  }
  .band {
    position: absolute;
    top: 855px; left: 0;
    width: 750px; height: 345px;
    background: var(--navy);
  }
  .headline {
    position: absolute;
    top: 24px; left: 30px;
    margin: 0;
    font-family: "Shippori Mincho B1", serif;
    font-weight: 600;
    color: var(--teal);
  }
  .headline .row1 { display: block; font-size: 114px; line-height: 132px; white-space: nowrap; }
  .headline .particle { font-size: 54px; }
  .headline .row2 { display: block; font-size: 114px; line-height: 132px; padding-left: 68px; white-space: nowrap; }
  .lead {
    position: absolute;
    top: 16px; right: 30px;
    margin: 0;
    writing-mode: vertical-rl;
    font-family: "Noto Sans JP", sans-serif;
    font-weight: 900;
    font-size: 42px;
    line-height: 50px;
    color: #fff;
    letter-spacing: 1px;
  }
</style>
</head>
<body>
<main class="cover">
  <p class="tagline">外国人と一緒に働くすべての人へ</p>
  <h1 class="title">
    <span>ミナト</span>
    <span>ハーモニー</span>
    <span>トーキング</span>
  </h1>
  <div class="title-en" lang="en">
    <span>Bright Harbor</span>
    <span>Dialogue</span>
  </div>
  <div class="author">
    <p class="author-role">外国人ブリッジコーディネーター</p>
    <p class="author-name">村上 健二</p>
  </div>
  <div class="photo" role="img" aria-label="オフィス街で笑顔でハイタッチする二人のビジネスマンの写真"></div>
  <section class="band">
    <h2 class="headline">
      <span class="row1">強い会社<span class="particle">を</span></span>
      <span class="row2">作る方法</span>
    </h2>
    <p class="lead">少子高齢化の<br>社会を生き残る</p>
  </section>
</main>
</body>
</html>
```